New Business Cards for Torvin Group

We need a new Business Card to compliment our new logo. We are a vibrant design, manufacture and install business providing recreation areas, public parks and Municipal spaces. We want business cards that are classy, modern and clean.

We have recently changed our logo, and are celebrating our 40th anniversary. We want business cards with a new modern design to reflect our status.

Target Market(s)

Customers

Contact Information for Business Card

We need all the details of our 3 offices as per the business card attached. Please disregard the old logo on the business card, the other three files show our new logo.

Requirements
Must have
• All info as per attached business card but with new logo.
Nice to have

```html
<!DOCTYPE html>
<html lang="en">
<head>
<meta charset="utf-8">
<title>Torvin Group – Business Cards</title>
<link rel="stylesheet" href="https://fonts.googleapis.com/css2?family=Archivo+Black&family=Arimo:wght@400;700&family=Source+Sans+3:wght@400&display=swap">
<style>
  :root {
    --page-bg: #ffffff;
    --card-grey: #808080;
    --card-gold: #d4aa24;
    --ink-dark: #434343;
    --ink-light: #ffffff;
    --accent-red: #e3343a;
    --heading-font: "Arimo", Arial, sans-serif;
    --title-font: "Archivo Black", "Arial Black", sans-serif;
    --body-font: "Source Sans 3", "Myriad Pro", sans-serif;
  }
  html, body {
    margin: 0;
    padding: 0;
    width: 1200px;
    height: 1000px;
    overflow: hidden;
    background: var(--page-bg);
  }
  .canvas {
    position: relative;
    width: 1200px;
    height: 1000px;
  }
  .icon-defs { position: absolute; width: 0; height: 0; }

  .card {
    position: absolute;
    left: 289px;
    width: 662px;
    height: 428px;
    border-radius: 52px;
    overflow: hidden;
  }
  .card--grey { top: 33px; background: var(--card-grey); }
  .card--gold { top: 517px; background: var(--card-gold); }

  /* brand */
  .brand {
    position: absolute;
    left: 40px;
    top: 78px;
    display: flex;
    align-items: center;
    gap: 14px;
  }
  .brand__mark {
    width: 44px;
    height: 44px;
    border-radius: 50%;
    background: var(--accent-red);
    flex: none;
  }
  .brand__name {
    margin: 0;
    font-family: var(--heading-font);
    font-weight: 700;
    font-size: 38px;
    line-height: 44px;
    color: var(--ink-dark);
    white-space: nowrap;
  }

  /* person */
  .person {
    position: absolute;
    left: 56px;
    top: 236px;
    width: 320px;
  }
  .person__name {
    margin: 0;
    font-family: var(--heading-font);
    font-weight: 700;
    font-size: 28px;
    line-height: 34px;
    color: var(--accent-red);
  }
  .person__role {
    margin: 8px 0 0;
    font-family: var(--body-font);
    font-size: 16px;
    line-height: 20px;
    color: var(--ink-light);
  }
  .person__contacts {
    list-style: none;
    margin: 22px 0 0;
    padding: 0;
  }
  .person__website {
    position: absolute;
    left: 56px;
    top: 383px;
    margin: 0;
    font-family: var(--heading-font);
    font-size: 18px;
    line-height: 22px;
    letter-spacing: 2.6px;
    color: var(--ink-light);
  }

  /* contact lines */
  .contact-line {
    position: relative;
    font-family: var(--body-font);
    font-size: 15px;
    line-height: 20.6px;
    color: var(--ink-dark);
    white-space: nowrap;
  }
  .contact-line .icon {
    position: absolute;
    top: 3px;
    width: 16px;
    height: 16px;
    fill: var(--ink-light);
  }
  .person__contacts .contact-line { padding-left: 21px; }
  .person__contacts .contact-line .icon { left: 0; }
  .office .contact-line .icon { left: -22px; }

  /* offices */
  .office {
    position: absolute;
    left: 406px;
    width: 250px;
  }
  .office--head { top: 25px; }
  .office--dubai { top: 163px; }
  .office--qatar { top: 305px; }
  .office__title {
    margin: 0;
    font-family: var(--title-font);
    font-weight: 400;
    font-size: 21px;
    line-height: 26px;
    color: var(--ink-dark);
  }
  .office__lines {
    list-style: none;
    margin: 0;
    padding: 0;
  }
</style>
</head>
<body>
<main class="canvas">

  <svg class="icon-defs" aria-hidden="true">
    <symbol id="icon-phone" viewBox="0 0 16 16">
      <path d="M3.5 1.5l2.4 2.6-1.3 1.8c.9 2 2.5 3.6 4.5 4.6l1.8-1.3 2.6 2.4-1.4 2.3c-5-.6-9.2-4.8-9.9-9.9z"/>
      <path d="M9 2a5 5 0 0 1 5 5h-1.2A3.8 3.8 0 0 0 9 3.2zM9 4.4A2.6 2.6 0 0 1 11.6 7h-1.2A1.4 1.4 0 0 0 9 5.6z"/>
    </symbol>
    <symbol id="icon-fax" viewBox="0 0 16 16">
      <path d="M4 1h8v4H4z"/>
      <path d="M1 6h14v6h-2v3H3v-3H1zM4.5 10v3.5h7V10z"/>
    </symbol>
    <symbol id="icon-mail" viewBox="0 0 16 16">
      <path d="M1 3.5h14v9H1zm1.4 1.2L8 8.9l5.6-4.2zM2.2 5.9v5.4h11.6V5.9L8 10.3z"/>
    </symbol>
    <symbol id="icon-mobile" viewBox="0 0 16 16">
      <path d="M4.5 1h7v14h-7zM5.8 2.6v6.2h4.4V2.6zM6 10.5h1.3v1.2H6zm2.7 0H10v1.2H8.7zM6 12.6h1.3v1.2H6zm2.7 0H10v1.2H8.7z"/>
    </symbol>
  </svg>

  <!-- grey card -->
  <article class="card card--grey">
    <div class="brand">
      <span class="brand__mark" aria-hidden="true"></span>
      <h1 class="brand__name">Torvin Group</h1>
    </div>

    <section class="person">
      <h2 class="person__name">Marek Dalvin</h2>
      <p class="person__role">Managing Partner</p>
      <ul class="person__contacts">
        <li class="contact-line"><svg class="icon"><use href="#icon-mobile"/></svg>+971 (0)50 384 7162</li>
        <li class="contact-line"><svg class="icon"><use href="#icon-mail"/></svg>marek@torvingroup.com</li>
      </ul>
    </section>
    <p class="person__website">www.torvingroup.com</p>

    <section class="office office--head">
      <h3 class="office__title">Head Office</h3>
      <ul class="office__lines">
        <li class="contact-line">P. o. Box: 48210 Abu Dhabi, U.A.E.</li>
        <li class="contact-line"><svg class="icon"><use href="#icon-phone"/></svg>+971 (0)2 5530127</li>
        <li class="contact-line"><svg class="icon"><use href="#icon-fax"/></svg>+971 (0)2 5530128</li>
        <li class="contact-line"><svg class="icon"><use href="#icon-mail"/></svg>sales@torvingroup.com</li>
      </ul>
    </section>
    <section class="office office--dubai">
      <h3 class="office__title">Dubai Office</h3>
      <ul class="office__lines">
        <li class="contact-line">P. o. Box: 271046 Dubai, U.A.E.</li>
        <li class="contact-line"><svg class="icon"><use href="#icon-phone"/></svg>+971 (0)4 3826405</li>
        <li class="contact-line"><svg class="icon"><use href="#icon-fax"/></svg>+971 (0)4 3826419</li>
        <li class="contact-line"><svg class="icon"><use href="#icon-mail"/></svg>sales@torvingroup.com</li>
      </ul>
    </section>
    <section class="office office--qatar">
      <h3 class="office__title">Qatar Office</h3>
      <ul class="office__lines">
        <li class="contact-line">P. o. Box: 30572 Doha, Qatar</li>
        <li class="contact-line"><svg class="icon"><use href="#icon-phone"/></svg>+971 4 40917382</li>
        <li class="contact-line"><svg class="icon"><use href="#icon-fax"/></svg>+971 4 40923518</li>
        <li class="contact-line"><svg class="icon"><use href="#icon-mail"/></svg>sales@torvingroup.com</li>
      </ul>
    </section>
  </article>

  <!-- gold card -->
  <article class="card card--gold">
    <div class="brand">
      <span class="brand__mark" aria-hidden="true"></span>
      <h1 class="brand__name">Torvin Group</h1>
    </div>

    <section class="person">
      <h2 class="person__name">Marek Dalvin</h2>
      <p class="person__role">Managing Partner</p>
      <ul class="person__contacts">
        <li class="contact-line"><svg class="icon"><use href="#icon-mobile"/></svg>+971 (0)50 384 7162</li>
        <li class="contact-line"><svg class="icon"><use href="#icon-mail"/></svg>marek@torvingroup.com</li>
      </ul>
    </section>
    <p class="person__website">www.torvingroup.com</p>

    <section class="office office--head">
      <h3 class="office__title">Head Office</h3>
      <ul class="office__lines">
        <li class="contact-line">P. o. Box: 48210 Abu Dhabi, U.A.E.</li>
        <li class="contact-line"><svg class="icon"><use href="#icon-phone"/></svg>+971 (0)2 5530127</li>
        <li class="contact-line"><svg class="icon"><use href="#icon-fax"/></svg>+971 (0)2 5530128</li>
        <li class="contact-line"><svg class="icon"><use href="#icon-mail"/></svg>sales@torvingroup.com</li>
      </ul>
    </section>
    <section class="office office--dubai">
      <h3 class="office__title">Dubai Office</h3>
      <ul class="office__lines">
        <li class="contact-line">P. o. Box: 271046 Dubai, U.A.E.</li>
        <li class="contact-line"><svg class="icon"><use href="#icon-phone"/></svg>+971 (0)4 3826405</li>
        <li class="contact-line"><svg class="icon"><use href="#icon-fax"/></svg>+971 (0)4 3826419</li>
        <li class="contact-line"><svg class="icon"><use href="#icon-mail"/></svg>sales@torvingroup.com</li>
      </ul>
    </section>
    <section class="office office--qatar">
      <h3 class="office__title">Qatar Office</h3>
      <ul class="office__lines">
        <li class="contact-line">P. o. Box: 30572 Doha, Qatar</li>
        <li class="contact-line"><svg class="icon"><use href="#icon-phone"/></svg>+971 4 40917382</li>
        <li class="contact-line"><svg class="icon"><use href="#icon-fax"/></svg>+971 4 40923518</li>
        <li class="contact-line"><svg class="icon"><use href="#icon-mail"/></svg>sales@torvingroup.com</li>
      </ul>
    </section>
  </article>

</main>
</body>
</html>
```